Up to the Challenge? Canadian based consulting company needs a two sided business card design

A Canadian based security risk management consulting company needs a two-sided business card design. What we do is provide advice and guidance related to emergency, security and business continuity management for small, medium and large companies to help ensure the protection of their people, assets, information, services, operations and reputation.

The final design should be simple, only one or two colours, eye catching, professional and one that makes people look at three or more times just because it looks so darn good.

I have include examples of business cards I like.

Target Market(s)

Small, medium and large companies.

Industry/Entity Type

Security

Contact Information for Business Card

Business Card Size: Standard size of 3.5" (89mm) x 2.0" (51mm) - (see full specifications and guides on PRINTA's website if required)
Card Stock: Looking to use PRINTA's Velda 32pt stock textured paper - seam colour either chili red or black
Business Name: The Harrowfield Group
Website: www.theharrowfieldgroup.example
Telephone: (555)214-0397
Name: Dana Forsythe
Position: Principle
e-mail: Dana.Forsythe@theharrowfieldgroup.example

Font styles to use
Serif

Colors
ec1f27
000000
9d9d9d
aaaaaa
606060

Requirements
Must have
• - "The Harrowfield Group" logo (see uploaded files). I have included grey scale and colour versions.
• - Business card details (as above)
Nice to have
• - One side black or grey scale.
• - Other side would likely be white.
• - Everyone likes the silver logo on the black background.
• - Small element of colour i.e. red but I'm leaning more to greyscale.
Should not have
• - A lot of colour. Keep it simple.

```html
<!DOCTYPE html>
<html lang="en">
<head>
<meta charset="utf-8">
<title>The Harrowfield Group — Business Card</title>
<link href="https://fonts.googleapis.com/css2?family=Cinzel:wght@400;600&display=swap" rel="stylesheet">
<style>
  :root {
    --backdrop: #5e5e5e;
    --card: #0c0c0c;
    --ink-raised: #2a2a2a;
    --ink-soft: #1c1c1c;
    --ink-text: #6a6a6a;
    --ink-title: #8a8a8a;
  }
  * { margin: 0; padding: 0; box-sizing: border-box; }
  html, body {
    width: 1200px;
    height: 918px;
    overflow: hidden;
    background: var(--backdrop);
    font-family: "Cinzel", serif;
  }
  .sheet {
    width: 1200px;
    height: 918px;
    display: flex;
    flex-direction: column;
    align-items: center;
    justify-content: center;
    gap: 38px;
  }
  .card {
    width: 700px;
    height: 400px;
    background: var(--card);
    position: relative;
    display: flex;
    flex-direction: column;
    align-items: center;
    justify-content: center;
  }
  .wordmark {
    display: flex;
    align-items: center;
    gap: 18px;
    color: var(--ink-raised);
    font-weight: 600;
    letter-spacing: 3px;
  }
  .wordmark__square {
    width: 34px;
    height: 34px;
    background: var(--ink-raised);
  }
  .card--front .wordmark { font-size: 34px; }
  .card--back .wordmark {
    font-size: 30px;
    color: var(--ink-soft);
    margin: 26px 0 30px;
  }
  .card--back .wordmark__square { background: var(--ink-soft); width: 28px; height: 28px; }
  .holder__name {
    font-size: 30px;
    font-weight: 600;
    color: var(--ink-title);
    letter-spacing: 1.5px;
  }
  .holder__role {
    font-size: 20px;
    font-weight: 600;
    color: var(--ink-text);
    letter-spacing: 1px;
    margin-top: 4px;
  }
  .contact {
    font-size: 17px;
    color: var(--ink-text);
    text-align: center;
    line-height: 1.9;
    letter-spacing: 0.5px;
  }
</style>
</head>
<body>
  <main class="sheet">
    <section class="card card--front" aria-label="Card front">
      <div class="wordmark">
        <span class="wordmark__square"></span>
        <span class="wordmark__name">THE HARROWFIELD GROUP</span>
      </div>
    </section>

    <section class="card card--back" aria-label="Card back">
      <h1 class="holder__name">DANA FORSYTHE</h1>
      <p class="holder__role">PRINCIPLE</p>
      <div class="wordmark">
        <span class="wordmark__square"></span>
        <span class="wordmark__name">THE HARROWFIELD GROUP</span>
      </div>
      <div class="contact">
        <p>P: (555)214-0397 | Dana.Forsythe@theharrowfieldgroup.example</p>
        <p>www.theharrowfieldgroup.example</p>
      </div>
    </section>
  </main>
</body>
</html>
```